Contemporary Vehicle wrap design

Looking for a contemporary design vehicle wrap. This is for a kitchen and bath remodeling company. We have a Brelm K-380 Truck, Brelm Ovaro Cargo Van and a 12’ enclosed trailer. Attached is our logo

Industry/Entity Type

Construction

Colors

Designer to choose colors to be used in the design.

```html
<!DOCTYPE html>
<html lang="en">
<head>
<meta charset="utf-8">
<title>CL design Kitchen + Bath — Vehicle Wrap</title>
<link href="https://fonts.googleapis.com/css2?family=Archivo:wght@400;600;700&family=Libre+Baskerville:ital,wght@1,700&display=swap" rel="stylesheet">
<style>
  :root {
    --teal: #1fd0c0;
    --ink: #161616;
    --graphite: #2a2a2a;
    --marble-light: #f4f4f4;
    --marble-mid: #dcdcdc;
    --stone-grey: #8a8a8a;
    --page: #ffffff;
  }
  * { margin: 0; padding: 0; box-sizing: border-box; }
  html, body { width: 1200px; height: 518px; overflow: hidden; background: var(--page); }
  .wrap {
    position: relative; width: 1200px; height: 518px;
    font-family: "Archivo", Arial, sans-serif; color: var(--ink);
    background:
      linear-gradient(160deg, rgba(0,0,0,0) 40%, rgba(0,0,0,.06) 44%, rgba(0,0,0,0) 48%),
      linear-gradient(20deg, rgba(0,0,0,0) 60%, rgba(0,0,0,.05) 63%, rgba(0,0,0,0) 66%),
      linear-gradient(180deg, var(--marble-light), var(--marble-mid));
  }
  .tagline-band {
    position: absolute; left: 0; top: 40px; width: 1200px; height: 52px;
    background: var(--teal);
    display: flex; align-items: center; justify-content: flex-end; gap: 14px;
    padding-right: 40px; font-size: 21px; font-weight: 700;
  }
  .tagline-band .serif { font-family: "Libre Baskerville", Georgia, serif; font-style: italic; font-size: 20px; }
  .tagline-band .caps { font-size: 22px; letter-spacing: .5px; }
  .kitchen-photo {
    position: absolute; left: 790px; top: 92px; width: 410px; height: 290px;
    background: linear-gradient(135deg, #d9dcdf 0%, #eef0f1 45%, #b9bdbf 80%, #8d8c88 100%);
  }
  .brand-box {
    position: absolute; left: 511px; top: 117px; width: 286px; height: 124px;
    border: 4px solid var(--ink);
    display: flex; align-items: center; justify-content: center;
    font-size: 44px; font-weight: 700; color: var(--ink); letter-spacing: 1px;
  }
  .service {
    position: absolute; left: 511px; top: 244px; width: 286px;
    font-size: 32px; font-weight: 600; letter-spacing: 1.5px; text-align: center;
  }
  .phone {
    position: absolute; left: 511px; top: 288px; width: 290px;
    font-size: 37px; font-weight: 400; white-space: nowrap;
  }
  .phone .word { color: var(--teal); font-weight: 700; }
  .follow {
    position: absolute; left: 288px; top: 298px; transform: rotate(-2deg);
  }
  .follow h2 { font-size: 17px; font-weight: 700; letter-spacing: .5px; margin-bottom: 8px; }
  .follow ul { list-style: none; display: flex; gap: 14px; }
  .follow li { display: flex; align-items: center; gap: 4px; font-size: 12px; font-weight: 600; }
  .follow .dot { width: 14px; height: 14px; background: var(--stone-grey); }
  .rocker-band {
    position: absolute; left: 0; top: 382px; width: 1200px; height: 30px; background: var(--graphite);
  }
  .web-strip {
    position: absolute; left: 0; top: 412px; width: 1200px; height: 40px;
    background: linear-gradient(180deg, var(--marble-light), var(--marble-mid));
    display: flex; align-items: center; padding-left: 436px;
    font-size: 25px; font-weight: 400; letter-spacing: .5px;
  }
  .base-band { position: absolute; left: 0; top: 452px; width: 1200px; height: 66px; background: var(--graphite); }
</style>
</head>
<body>
  <main class="wrap">
    <div class="tagline-band">
      <span>Making Dreams A Reality</span>
      <span class="serif">Over 3 Decades of</span>
      <span class="caps">COMBINED EXPERIENCE</span>
    </div>
    <div class="kitchen-photo" role="img" aria-label="Photo of a finished white kitchen with shaker cabinets, marble counters and a window sink"></div>
    <div class="brand-box">CL design</div>
    <div class="service">KITCHEN + BATH</div>
    <div class="phone">(555) 01-<span class="word">STONE</span></div>
    <section class="follow">
      <h2>FOLLOW US ON</h2>
      <ul>
        <li><span class="dot"></span>Friendly</li>
        <li><span class="dot"></span>Pixelgram</li>
        <li><span class="dot"></span>Chirper</li>
      </ul>
    </section>
    <div class="rocker-band"></div>
    <div class="web-strip">www.calderlinndesign.com</div>
    <div class="base-band"></div>
  </main>
</body>
</html>
```